Graphic to communicate emotional connection

Howdy-I need a graphic that describe my financial planning process.The attached is a concept, but please use your own creativity to show how you would display this:- The four circles on the outside (Protect what we have, know where it goes, make it grow, and dignity and independence) are the four major areas of concern- Then, there are three value statements:- The first is the most powerful which is that Clarity leads to Control which allows your Intentions to come through- The second shows that we take our clients from Uncertainty and Confusion, to Confidence and Intention- The third says we create space for you to develop your Purposeful Effort which leads to Your Best Financial Life.I've also attached my logo - please use the colors in my logo and maybe add a soft green as needed.The reader should be able to briefly scan this document and understand that we will connect with them on an emotional level to get their finances in shape.Thanks!-Ned

Target Market(s)

wealthy women, whether independent or married

Industry/Entity Type

Financial Planning

Requirements
Must have
• Please use the colors in my logo plus a soft green as needed
Should not have
• This should not be a busy or hard-to-read graphic. It is meant to convey an that I try to make an emotional connection, at a glance.

```html
<!DOCTYPE html>
<html lang="en">
<head>
<meta charset="utf-8">
<title>Harbor Lane Wealth – Planning Process</title>
<link href="https://fonts.googleapis.com/css2?family=Archivo+Black&family=Libre+Baskerville:ital@0;1&display=swap" rel="stylesheet">
<style>
  :root{
    --navy:#0b3a7d;
    --slate:#6d6e71;
    --leaf:#8cc63f;
    --mat:#231f20;
    --paper:#ffffff;
    --rule:#e6e7e8;
  }
  html,body{margin:0;padding:0;width:916px;height:1200px;overflow:hidden;background:var(--mat);}
  .stage{position:absolute;left:0;top:0;width:962px;height:1260px;transform:scale(0.95218);transform-origin:0 0;background:var(--mat);}
  .sheet{position:absolute;left:114px;top:104px;width:736px;height:1052px;background:var(--paper);}
  .sheet-frame{position:absolute;left:152px;top:144px;width:644px;height:956px;border:8px solid var(--rule);}
  .brand{position:absolute;left:0;width:962px;top:186px;text-align:center;font-family:"Libre Baskerville",serif;color:var(--navy);font-size:28px;letter-spacing:1px;}
  .brand-mark{display:inline-block;width:22px;height:22px;background:var(--navy);margin-right:12px;vertical-align:-2px;}
  .process{position:absolute;left:0;top:0;}
  .ring-word{font-family:"Archivo Black",sans-serif;font-size:50px;fill:var(--paper);}
  .ring-note{font-family:"Archivo Black",sans-serif;font-size:16px;fill:var(--slate);}
  .core{position:absolute;left:268px;width:400px;text-align:center;font-family:"Archivo Black",sans-serif;color:#666769;font-size:54px;letter-spacing:-2px;line-height:1;}
  .core-clarity{top:464px;}
  .core-control{top:536px;}
  .core-intention{top:608px;}
  .core-arrow{position:absolute;left:457px;width:10px;height:18px;}
  .lead{position:absolute;font-family:"Libre Baskerville",serif;font-style:italic;font-size:13px;color:var(--slate);}
  .from{position:absolute;font-family:"Archivo Black",sans-serif;font-size:28px;line-height:25px;color:var(--navy);letter-spacing:-0.5px;}
  .from.right{text-align:right;}
  .shift-arrow{position:absolute;left:416px;width:98px;height:64px;}
  .site{position:absolute;left:0;width:962px;top:1124px;text-align:center;font-family:"Libre Baskerville",serif;font-size:13px;color:var(--slate);letter-spacing:0.5px;}
</style>
</head>
<body>
<div class="stage">
  <div class="sheet"></div>
  <div class="sheet-frame"></div>

  <div class="brand"><span class="brand-mark"></span>HARBOR LANE WEALTH</div>

  <svg class="process" width="962" height="1260" viewBox="0 0 962 1260">
    <defs>
      <path id="arc-top-inner" d="M260,568 A208,208 0 1 1 676,568 A208,208 0 1 1 260,568"/>
      <path id="arc-bottom-inner" d="M224,568 A244,244 0 1 0 712,568 A244,244 0 1 0 224,568"/>
      <path id="arc-top-outer" d="M179,568 A289,289 0 1 1 757,568 A289,289 0 1 1 179,568"/>
      <path id="arc-bottom-outer" d="M167,568 A301,301 0 1 0 769,568 A301,301 0 1 0 167,568"/>
    </defs>
    <g fill="var(--navy)">
      <path class="seg-protect" d="M191.5,584.9 A277,277 0 0 1 460.7,291.1 L481.8,342.4 L463.4,393.1 A175,175 0 0 0 293.3,578.7 L242.1,562.1 Z"/>
      <path class="seg-dignity" d="M475.3,291.1 A277,277 0 0 1 742.0,527.1 L693.6,554.2 L641.1,542.1 A175,175 0 0 0 472.6,393.1 L493.6,343.5 Z"/>
      <path class="seg-grow" d="M743.7,541.4 A277,277 0 0 1 513.7,841.2 L485.7,793.3 L496.9,740.6 A175,175 0 0 0 642.2,551.2 L694.0,566.0 Z"/>
      <path class="seg-know" d="M499.4,843.2 A277,277 0 0 1 192.8,599.4 L242.1,573.9 L294.1,587.8 A175,175 0 0 0 487.8,741.9 L473.9,793.9 Z"/>
    </g>
    <rect x="458" y="285" width="20" height="112" fill="var(--paper)"/>
    <circle cx="468" cy="345" r="38" fill="var(--paper)"/>
    <circle cx="468" cy="345" r="18" fill="var(--navy)"/>

    <text class="ring-word"><textPath href="#arc-top-inner" startOffset="11.7%" text-anchor="middle">PROTECT</textPath></text>
    <text class="ring-word"><textPath href="#arc-top-inner" startOffset="37.5%" text-anchor="middle">DIGNITY</textPath></text>
    <text class="ring-word"><textPath href="#arc-bottom-inner" startOffset="15.3%" text-anchor="middle">KNOW</textPath></text>
    <text class="ring-word"><textPath href="#arc-bottom-inner" startOffset="38.9%" text-anchor="middle">GROW</textPath></text>

    <text class="ring-note"><textPath href="#arc-top-outer" startOffset="11.4%" text-anchor="middle">PROTECT WHAT WE HAVE</textPath></text>
    <text class="ring-note"><textPath href="#arc-top-outer" startOffset="41%" text-anchor="middle">DIGNITY AND INDEPENDENCE</textPath></text>
    <text class="ring-note"><textPath href="#arc-bottom-outer" startOffset="12.8%" text-anchor="middle">KNOW WHERE IT GOES</textPath></text>
    <text class="ring-note"><textPath href="#arc-bottom-outer" startOffset="37.8%" text-anchor="middle">MAKE IT GROW</textPath></text>
  </svg>

  <div class="core core-clarity">Clarity</div>
  <svg class="core-arrow" style="top:516px" viewBox="0 0 10 18"><path d="M3,0 H7 V10 H10 L5,18 L0,10 H3 Z" fill="var(--navy)"/></svg>
  <div class="core core-control">Control</div>
  <svg class="core-arrow" style="top:586px" viewBox="0 0 10 18"><path d="M3,0 H7 V10 H10 L5,18 L0,10 H3 Z" fill="var(--navy)"/></svg>
  <div class="core core-intention">Intention</div>

  <div class="lead" style="right:552px;top:898px;">We take you from</div>
  <div class="from right" style="right:552px;top:918px;">Uncertainty<br>Confusion</div>
  <svg class="shift-arrow" style="top:914px" viewBox="0 0 98 64"><polygon points="0,10 66,10 66,0 98,32 66,64 66,54 0,54" fill="var(--leaf)"/></svg>
  <div class="lead" style="left:530px;top:902px;">To</div>
  <div class="from" style="left:523px;top:918px;">Confidence<br>Intention</div>

  <div class="lead" style="right:552px;top:1006px;">We create space for you</div>
  <div class="from right" style="right:552px;top:1023px;">Purposeful<br>Effort</div>
  <svg class="shift-arrow" style="top:1018px" viewBox="0 0 98 64"><polygon points="0,10 66,10 66,0 98,32 66,64 66,54 0,54" fill="var(--leaf)"/></svg>
  <div class="lead" style="left:530px;top:1005px;">Which leads to you</div>
  <div class="from" style="left:531px;top:1023px;">Best<br>Financial Life</div>

  <div class="site">WWW.HARBORLANEWEALTH.COM</div>
</div>
</body>
</html>
```